family chiropractic health care team needs a modern business card design

Healthcare office with Chiropractors, Physiotherapists, Massage therapists and possibly other practitioners in the future. This is a friendly family office with patients of all ages (and lots of kids) that just moved into a new larger modern office.
Look at the website for photos of the office.
Design for the front and back of a business card required.
Text for the front:
Office logo and name of the office:
Bright Path Wellness Centre
Name of current Practitioner:
Dr. Marten Quovel B.Sc., D.C. Chiropractor
(But please include options to swap out name and title for other practitioners )

address:
218 Farrow Gate
Etobicoke ON.
K2J 6P4
Phone: 416-872-0196 (PATH)
Web site and email:
www.brightpathwellnesscentre.example
brightpathchiro@mailbox.example

2 versions of the back of the card:
1. text below
2. appointment schedule card

Text on back of card:
Chiropractic Card text on back of the card:
There is more to chiropractic than the relief of headaches and back pain! Our primary focus is the integrity of your nerve system, which controls and regulates every cell and tissue of your body. The moving bones of the spinal column can impair this vital communication link between your brain and body. We help improve the function and structure of your spine, reducing nerve system compromise. The result?
Even non-spinal related health problems can show improvement
without drugs
without surgery
regardless of age
for over a century
naturally

Appointment Card info For Back:
Please integrate design elements from the front of the card into an appointment card format.
M Tu W Th F Sat (and a line for writing on beside each one)

```html
<!DOCTYPE html>
<html lang="en">
<head>
<meta charset="utf-8">
<title>Bright Path Wellness Centre – Business Card</title>
<link rel="stylesheet" href="https://fonts.googleapis.com/css2?family=Montserrat:wght@300;400;600&display=swap">
<style>
  :root {
    --page-bg: #2a2a2c;
    --card-bg: #141414;
    --card-bg-edge: #1c1c1c;
    --leaf-green: #7cc242;
    --leaf-green-deep: #2f4a1c;
    --text-light: #e8e8e8;
    --text-muted: #cfcfcf;
  }
  * { box-sizing: border-box; margin: 0; padding: 0; }
  html, body {
    width: 1200px;
    height: 900px;
    overflow: hidden;
    background: var(--page-bg);
    font-family: "Montserrat", sans-serif;
  }
  .sheet {
    width: 1200px;
    height: 900px;
    display: flex;
    flex-direction: column;
    align-items: center;
    justify-content: center;
    gap: 40px;
  }
  .card {
    width: 700px;
    height: 400px;
    border-radius: 22px;
    background: linear-gradient(160deg, var(--card-bg-edge), var(--card-bg));
    position: relative;
    overflow: hidden;
    box-shadow: 0 18px 40px rgba(0,0,0,0.45);
  }
  .card-back__pattern {
    position: absolute;
    inset: 0;
    background: linear-gradient(200deg, #111 0%, #161a13 45%, var(--leaf-green-deep) 80%, #5f9433 100%);
  }
  .card-front__brand {
    position: absolute;
    left: 48px;
    top: 262px;
    display: flex;
    align-items: center;
    gap: 10px;
  }
  .brand__dot {
    width: 14px;
    height: 14px;
    border-radius: 50%;
    background: var(--leaf-green);
    flex: none;
  }
  .brand__name {
    font-weight: 600;
    font-size: 19px;
    color: var(--leaf-green);
    letter-spacing: 0.3px;
    line-height: 1.2;
    width: 230px;
  }
  .card-front__divider {
    position: absolute;
    left: 330px;
    top: 78px;
    width: 2px;
    height: 250px;
    background: var(--leaf-green);
  }
  .card-front__details {
    position: absolute;
    left: 356px;
    top: 76px;
    right: 20px;
    color: var(--text-light);
  }
  .practitioner__name {
    font-weight: 600;
    font-size: 21px;
    color: var(--leaf-green);
    line-height: 1.15;
  }
  .practitioner__title {
    font-weight: 300;
    font-size: 14px;
    margin-top: 4px;
    color: var(--text-muted);
  }
  .address {
    font-style: normal;
    font-weight: 300;
    font-size: 14px;
    line-height: 1.35;
    margin-top: 22px;
  }
  .contact-list {
    list-style: none;
    margin-top: 22px;
    font-weight: 300;
    font-size: 12.5px;
  }
  .contact-list__item {
    display: flex;
    align-items: center;
    gap: 10px;
    margin-bottom: 7px;
    white-space: nowrap;
  }
  .contact-list__icon {
    width: 13px;
    height: 13px;
    flex: none;
  }
</style>
</head>
<body>
<main class="sheet">
  <section class="card card-back" aria-label="Card back">
    <div class="card-back__pattern" role="img" aria-label="Repeating leaf pattern fading from bright green in the lower left to black"></div>
  </section>

  <section class="card card-front" aria-label="Card front">
    <div class="card-front__brand">
      <span class="brand__dot"></span>
      <span class="brand__name">Bright Path Wellness Centre</span>
    </div>

    <div class="card-front__divider"></div>

    <div class="card-front__details">
      <h1 class="practitioner__name">Dr. Marten Quovel B.Sc</h1>
      <p class="practitioner__title">D.C. Chiropractor</p>

      <address class="address">
        218 Farrow Gate<br>
        Etobicoke ON.<br>
        K2J 6P4
      </address>

      <ul class="contact-list">
        <li class="contact-list__item">
          <svg class="contact-list__icon" viewBox="0 0 16 16" aria-hidden="true">
            <path fill="#7cc242" d="M3.6 1.5l2.2 2.6-1.3 1.6c.9 2 2.4 3.5 4.4 4.4l1.6-1.3 2.6 2.2-1.2 2.3C6.5 13.2 2.8 9.5 1.3 2.7z"/>
          </svg>
          416-872-0196 (PATH)
        </li>
        <li class="contact-list__item">
          <svg class="contact-list__icon" viewBox="0 0 16 16" aria-hidden="true">
            <rect x="1" y="3" width="14" height="10" rx="1" fill="#7cc242"/>
            <path d="M1.5 3.8L8 9l6.5-5.2" stroke="#141414" stroke-width="1.3" fill="none"/>
          </svg>
          brightpathchiro@mailbox.example
        </li>
        <li class="contact-list__item">
          <svg class="contact-list__icon" viewBox="0 0 16 16" aria-hidden="true">
            <circle cx="8" cy="8" r="6.5" fill="none" stroke="#7cc242" stroke-width="1.5"/>
            <ellipse cx="8" cy="8" rx="2.8" ry="6.5" fill="none" stroke="#7cc242" stroke-width="1.2"/>
            <path d="M1.5 8h13" stroke="#7cc242" stroke-width="1.2"/>
          </svg>
          www.brightpathwellnesscentre.example
        </li>
      </ul>
    </div>
  </section>
</main>
</body>
</html>
```